" A EMPRESA ATUA NO SEGMENTO DE OUTSOURCING DE PRINTIAÃO: LOCAÇÃO DE IMPRESSORAS E MULTIFUNCIONAIS, E IMPLANTAÇÃO DE SOFTWARES AGREGADOS A ESSAS MÁQUINAS. "

```html
<!DOCTYPE html>
<html lang="pt-BR">
<head>
<meta charset="UTF-8">
<title>Assinatura de e-mail — PRINTIA</title>
<link rel="stylesheet" href="https://fonts.googleapis.com/css2?family=Montserrat:wght@400;500;600;700&display=swap">
<style>
  :root{
    --navy:#1b2a5c;
    --ink:#2b2f3a;
    --muted:#6b6f78;
    --line-grey:#c9ccd3;
    --tagline:#8fb0e6;
    --paper:#ffffff;
  }
  html,body{margin:0;padding:0;width:1200px;height:1200px;overflow:hidden;background:var(--paper);}
  body{font-family:"Montserrat",sans-serif;color:var(--ink);position:relative;}
  .signature{position:absolute;left:60px;top:460px;width:1080px;height:280px;}
  .signature__band{position:absolute;right:0;top:0;width:660px;height:280px;}
  .brand{position:absolute;left:640px;top:92px;display:flex;flex-direction:column;align-items:flex-start;}
  .brand__name{color:#fff;font-weight:600;font-size:62px;line-height:1;letter-spacing:1px;}
  .brand__tagline{color:var(--tagline);font-weight:500;font-size:19px;letter-spacing:1.5px;margin-top:8px;}
  .person{position:absolute;left:0;top:20px;}
  .person__head{border-left:6px solid var(--navy);padding-left:14px;}
  .person__name{font-weight:600;font-size:30px;color:var(--navy);letter-spacing:.5px;line-height:1.15;}
  .person__role{font-size:22px;color:var(--muted);margin-top:4px;}
  .contacts{list-style:none;margin:26px 0 0;padding:0;}
  .contacts__item{display:flex;align-items:flex-start;gap:14px;font-size:17px;color:var(--ink);margin-bottom:12px;line-height:1.15;}
  .contacts__icon{width:24px;height:24px;background:var(--navy);flex:none;display:flex;align-items:center;justify-content:center;}
  .contacts__icon svg{width:16px;height:16px;}
</style>
</head>
<body>
  <section class="signature" aria-label="Assinatura de e-mail">
    <svg class="signature__band" viewBox="0 0 660 280" aria-hidden="true">
      <path d="M8 0 C 50 150 120 250 238 280" fill="none" stroke="var(--line-grey)" stroke-width="10"/>
      <path d="M24 0 L660 0 L660 280 L250 280 C 140 250 70 150 24 0 Z" fill="var(--navy)"/>
    </svg>

    <div class="brand">
      <span class="brand__name">PRINTIA</span>
      <span class="brand__tagline">OUTSOURCING DE IMPRESSÃO</span>
    </div>

    <div class="person">
      <div class="person__head">
        <div class="person__name">NOME E SOBRENOME</div>
        <div class="person__role">Cargo | Função</div>
      </div>
      <ul class="contacts">
        <li class="contacts__item">
          <span class="contacts__icon"><svg viewBox="0 0 16 16"><path d="M4 2 L6.5 2 L7.5 5 L6 6.2 C6.8 8 8 9.2 9.8 10 L11 8.5 L14 9.5 L14 12 C14 13 13 14 12 14 C7 14 2 9 2 4 C2 3 3 2 4 2 Z" fill="#fff"/></svg></span>
          <span>(00) 0000-0000</span>
        </li>
        <li class="contacts__item">
          <span class="contacts__icon"><svg viewBox="0 0 16 16"><rect x="2" y="4" width="12" height="9" fill="#fff"/><path d="M2 4 L8 9 L14 4" fill="none" stroke="var(--navy)" stroke-width="1.4"/></svg></span>
          <span>contato@exemplo.com</span>
        </li>
        <li class="contacts__item">
          <span class="contacts__icon"><svg viewBox="0 0 16 16"><circle cx="8" cy="8" r="6" fill="none" stroke="#fff" stroke-width="1.5"/><ellipse cx="8" cy="8" rx="2.6" ry="6" fill="none" stroke="#fff" stroke-width="1.2"/><line x1="2" y1="8" x2="14" y2="8" stroke="#fff" stroke-width="1.2"/></svg></span>
          <span>www.exemplo.com.br</span>
        </li>
        <li class="contacts__item">
          <span class="contacts__icon"><svg viewBox="0 0 16 16"><path d="M8 15 C5 11 3.5 8.5 3.5 6 A4.5 4.5 0 0 1 12.5 6 C12.5 8.5 11 11 8 15 Z" fill="#fff"/><circle cx="8" cy="6" r="1.7" fill="var(--navy)"/></svg></span>
          <span>rua exemplo, sl 000<br>cidade-UF, CEP: 00000-000</span>
        </li>
      </ul>
    </div>
  </section>
</body>
</html>
```